Employee engagement survey desk drop

We want to get employees excited about the upcoming employee engagement survey so as part of our campaign we will be doing a desk drop/flyer. The final print size is 5.5" tall x 8.5" wide so need the final layout to be 2-up on an 8.5 x 11 (letter-size) paper. Other specs: one-sided, 4-color. The theme is "engagement" and this piece will accompany a candy "glim drop" (think engagement ring).
Updates

Following is proposed content for the piece. Feel free to edit the body copy to fit the design theme, if needed. BODY COPY: Corvessa is deeply committed to our employees and we want to take this relationship to the next level. Therefore, it’s time for a proper proposal: will you, Corvessa employee, take the annual employee engagement survey? We want to understand your feelings, experiences, and ideas for ways to ways to strengthen and fortify our relationship. ADDITIONAL DETAILS: You will receive an email on June 6, 2018 with a link to the employee engagement survey. Please complete the survey by June 26, 2018.

Target Market(s)

Employees

Requirements
Must have
• 1.) Should mention "Corvessa Employee Engagement Survey"
• 2.) The logo provided should be a smaller element in the overall design.
Nice to have
• 1.) I've attached our brand guidelines with color and font details. It's not necessary to use only the colors available in our palette but where you do use these colors, please refer to this document. For example, if you are using red, use CMYK 3-100-59-12.
• 2.) You do not have to use the fonts outlined in the brand guidelines, if they don't match the design. Feel free to use more romantic fonts (decorative or script) if they fit better.
• 3.) Corvessa is a hearing health/hearing aid company whose tagline is "bringing sound to life" so any ideas that could incorporate that theme as well as the ring would be cool.

```html
<!DOCTYPE html>
<html lang="en">
<head>
<meta charset="utf-8">
<title>Corvessa Employee Engagement Survey – Desk Drop</title>
<link rel="stylesheet" href="https://fonts.googleapis.com/css2?family=Open+Sans:wght@300;400&family=Playfair+Display+SC:wght@400&display=swap">
<style>
  :root {
    --crimson: #c4003f;
    --crimson-deep: #9e0033;
    --rose: #e25a86;
    --ink: #2b2b2b;
    --body-grey: #6b6b6b;
    --paper: #ffffff;
    --skin-light: #efd9cc;
    --skin-mid: #d9b7a4;
    --linen: #f4f2f0;
  }
  * { box-sizing: border-box; margin: 0; padding: 0; }
  html, body { width: 865px; height: 1200px; overflow: hidden; background: var(--paper); }
  .flyer { position: relative; width: 865px; height: 1200px; background: var(--paper); overflow: hidden; font-family: "Open Sans", sans-serif; }

  .hero-photo {
    position: absolute; top: 0; left: 0; width: 865px; height: 600px;
    background: linear-gradient(135deg, var(--linen) 0%, var(--skin-light) 35%, var(--skin-mid) 60%, var(--linen) 100%);
  }
  .hero-wave { position: absolute; left: 0; top: 380px; width: 865px; height: 250px; }

  .title-block {
    position: absolute; top: 630px; left: 0; width: 865px; text-align: center;
  }
  .campaign-title {
    font-family: "Open Sans", sans-serif; font-weight: 300; font-size: 46px;
    line-height: 1.1; color: var(--ink); letter-spacing: 3px; text-transform: uppercase;
  }
  .brand-line {
    margin-top: 10px; font-family: "Open Sans", sans-serif; font-weight: 400;
    font-size: 18px; color: var(--crimson); letter-spacing: 1px;
  }

  .body-copy {
    position: absolute; top: 765px; left: 90px; width: 685px;
    font-size: 16.5px; font-weight: 300; line-height: 1.45; color: var(--body-grey); text-align: center;
  }

  .details { position: absolute; top: 930px; left: 0; width: 865px; text-align: center; color: var(--body-grey); }
  .details p { font-size: 24px; font-weight: 300; line-height: 1.3; }
  .date { font-family: "Playfair Display SC", serif; font-size: 36px; color: var(--crimson); line-height: 1.15; letter-spacing: 1px; }
  .detail-divider { width: 320px; height: 14px; margin: 10px auto 8px; display: block; }
</style>
</head>
<body>
<main class="flyer">
  <div class="hero-photo" role="img" aria-label="Close-up photograph of two clasped hands wearing wedding rings"></div>

  <svg class="hero-wave" viewBox="0 0 865 250" preserveAspectRatio="none" aria-hidden="true">
    <defs>
      <linearGradient id="swoosh" x1="0" y1="0" x2="1" y2="0">
        <stop offset="0" stop-color="#9e0033"/>
        <stop offset="0.6" stop-color="#c4003f"/>
        <stop offset="1" stop-color="#e25a86"/>
      </linearGradient>
    </defs>
    <path d="M0 170 C220 110 420 200 600 120 C720 70 800 40 865 20 L865 250 L0 250 Z" fill="url(#swoosh)"/>
    <path d="M0 205 C240 150 430 225 610 160 C720 120 800 95 865 85 L865 250 L0 250 Z" fill="#ffffff"/>
  </svg>

  <header class="title-block">
    <h1 class="campaign-title">Your Voice</h1>
    <p class="brand-line">Corvessa Employee Engagement Survey</p>
  </header>

  <p class="body-copy">Corvessa is deeply committed to our employees and we want to take this relationship to the next level. Therefore, it’s time for a proper proposal: will you, Corvessa employee, take the annual employee engagement survey? We want to understand your feelings, experiences, and ideas for ways to ways to strengthen and fortify our relationship.</p>

  <section class="details">
    <p>You will receive an email on</p>
    <div class="date">June 6, 2018</div>
    <p>with a link to the employee engagement survey.</p>
    <svg class="detail-divider" viewBox="0 0 320 14" aria-hidden="true">
      <line x1="0" y1="7" x2="148" y2="7" stroke="#c4003f" stroke-width="1"/>
      <rect x="155" y="2" width="10" height="10" transform="rotate(45 160 7)" fill="#c4003f"/>
      <line x1="172" y1="7" x2="320" y2="7" stroke="#c4003f" stroke-width="1"/>
    </svg>
    <p>Please complete the survey by</p>
    <div class="date">June 26, 2018.</div>
  </section>
</main>
</body>
</html>
```